GreenHarborPeak - Double Sided Business Card

We are looking for design options or our business cards. We are a Business Solutions and HR solutions Provider - the theme is business, for this card.

Our brand colours are represented within our logo.

Details needed to be put on the front of the business card are:

Employees name: [Sample Name]
Role: [Sample Role]

Address: Suite 4 - Level 3/48 Lindqvist Avenue Kestrel Vale NSW 2199
M: 0000 000 000
P: 1300 482 917
F: 1300 482 935
E: sample@greenharborpeak.com.au
www.greenharborpeak.com.au

Reason: Hello, could we please increase our deadline by 5 days. Thanking you, Tamsin

Target Market(s)

Business Owners, also Candidates looking for Employment

Industry/Entity Type

Business

Contact Information for Business Card

Role: [Sample Role]

M: 0000 000 000
P: 1300 482 917
F: 1300 482 935

Font styles to use
Sans Serif

Colors
3276b5
3176b5
0455a3
85abd2
cfdeed
ffffff
000000
1b1b1b
757575

Requirements
Must have
• Details needed to be put on the front of the business card are:
• Employees name: [Sample Name]
• Role: [Sample Role]
• Address: Suite 4 - Level 3/48 Lindqvist Avenue Kestrel Vale NSW 2199
• M: 0000 000 000
• P: 1300 482 917
• F: 1300 482 935
• E: sample@greenharborpeak.com.au
• www.greenharborpeak.com.au
Nice to have
• Simplicity, clean and professional.

```html
<!DOCTYPE html>
<html lang="en">
<head>
<meta charset="utf-8">
<title>GreenHarborPeak – Business Card</title>
<link rel="stylesheet" href="https://fonts.googleapis.com/css2?family=Roboto:wght@400;500;700;900&display=swap">
<style>
  :root {
    --stage: #2a2a2a;
    --card: #1b1b1b;
    --emboss: #3a3a3a;
    --white: #ffffff;
    --blue: #3276b5;
    --blue-deep: #0455a3;
    --blue-light: #85abd2;
    --blue-pale: #cfdeed;
    --grey: #757575;
  }
  html, body {
    margin: 0;
    padding: 0;
    width: 799px;
    height: 1200px;
    overflow: hidden;
    background: var(--stage);
    font-family: "Roboto", Arial, sans-serif;
  }
  .canvas {
    position: relative;
    width: 799px;
    height: 1200px;
  }
  .card {
    position: absolute;
    left: 80px;
    width: 640px;
    height: 390px;
    background: var(--card);
    overflow: hidden;
    box-shadow: 0 6px 18px rgba(0,0,0,0.45);
  }
  .card--front { top: 95px; }
  .card--back { top: 705px; }

  /* Front */
  .front-mark {
    position: absolute;
    inset: 0;
    display: flex;
    align-items: center;
    justify-content: center;
    gap: 14px;
  }
  .front-mark__square {
    width: 34px;
    height: 34px;
    background: var(--emboss);
  }
  .front-mark__name {
    font-weight: 700;
    font-size: 40px;
    color: var(--emboss);
    letter-spacing: 0.5px;
  }

  /* Back */
  .bands {
    position: absolute;
    inset: 0;
  }
  .brand {
    position: absolute;
    left: 30px;
    top: 34px;
    display: flex;
    align-items: center;
    gap: 16px;
  }
  .brand__square {
    width: 64px;
    height: 64px;
    background: var(--blue);
  }
  .brand__name {
    font-weight: 700;
    font-size: 38px;
    color: var(--white);
    letter-spacing: 0.5px;
  }
  .tagline {
    position: absolute;
    left: 110px;
    top: 110px;
    width: 480px;
    margin: 0;
    padding-top: 6px;
    border-top: 1px solid var(--white);
    font-weight: 700;
    font-size: 13px;
    color: var(--white);
  }
  .person {
    position: absolute;
    left: 30px;
    top: 196px;
    color: var(--white);
  }
  .person__name {
    font-weight: 700;
    font-size: 26px;
    margin: 0;
  }
  .person__role {
    font-size: 14px;
    margin: 4px 0 0;
  }
  .contact {
    position: absolute;
    left: 360px;
    top: 176px;
    color: var(--white);
    font-size: 15px;
    line-height: 20px;
  }
  .contact__address {
    margin: 0 0 6px 20px;
  }
  .contact__list {
    list-style: none;
    margin: 0;
    padding: 0;
  }
  .contact__item {
    display: flex;
    align-items: center;
    gap: 10px;
  }
  .contact__icon {
    width: 14px;
    height: 14px;
    flex: none;
  }
  .website {
    position: absolute;
    left: 300px;
    top: 340px;
    width: 330px;
    margin: 0;
    text-align: center;
    font-weight: 500;
    font-size: 17px;
    color: var(--white);
  }
</style>
</head>
<body>
<main class="canvas">

  <section class="card card--front" aria-label="Business card front">
    <div class="front-mark">
      <span class="front-mark__square"></span>
      <span class="front-mark__name">GreenHarborPeak</span>
    </div>
  </section>

  <section class="card card--back" aria-label="Business card back">
    <svg class="bands" viewBox="0 0 640 390" width="640" height="390" aria-hidden="true">
      <polygon points="0,264 250,264 268,286 0,286" fill="var(--blue-light)"/>
      <polygon points="262,322 640,322 640,390 300,390" fill="var(--blue-deep)"/>
    </svg>

    <div class="brand">
      <span class="brand__square"></span>
      <span class="brand__name">GreenHarborPeak</span>
    </div>
    <p class="tagline">Guiding small and growing firms toward lasting success</p>

    <div class="person">
      <p class="person__name">Sample Name</p>
      <p class="person__role">Managing Director</p>
    </div>

    <div class="contact">
      <p class="contact__address">Suite 4 - Level 3/48 Lindqvist Avenue<br>Kestrel Vale NSW 2199</p>
      <ul class="contact__list">
        <li class="contact__item">
          <svg class="contact__icon" viewBox="0 0 14 14" aria-hidden="true"><rect x="3" y="0.5" width="8" height="13" rx="1.5" fill="var(--blue-light)"/><rect x="4.5" y="2" width="5" height="8" fill="var(--card)"/></svg>
          <span>0000 000 000</span>
        </li>
        <li class="contact__item">
          <svg class="contact__icon" viewBox="0 0 14 14" aria-hidden="true"><path d="M1 4 Q7 0 13 4 L12 6 L9.5 5 L9.5 4 Q7 3 4.5 4 L4.5 5 L2 6 Z" fill="var(--blue-light)"/><rect x="2" y="7" width="10" height="6" rx="1" fill="var(--blue-light)"/></svg>
          <span>1300 482 917</span>
        </li>
        <li class="contact__item">
          <svg class="contact__icon" viewBox="0 0 14 14" aria-hidden="true"><rect x="3.5" y="0.5" width="7" height="4" fill="var(--blue-light)"/><rect x="0.5" y="5" width="13" height="6" rx="1" fill="var(--blue-light)"/><rect x="3.5" y="9" width="7" height="4.5" fill="var(--blue-pale)"/></svg>
          <span>1300 482 935</span>
        </li>
        <li class="contact__item">
          <svg class="contact__icon" viewBox="0 0 14 14" aria-hidden="true"><rect x="0.5" y="3" width="13" height="9" fill="var(--blue-light)"/><path d="M0.5 3 L7 8 L13.5 3" fill="none" stroke="var(--card)" stroke-width="1.2"/></svg>
          <span>sample@greenharborpeak.com.au</span>
        </li>
      </ul>
    </div>

    <p class="website">www.greenharborpeak.com.au</p>
  </section>

</main>
</body>
</html>
```